Commercial and Residential Paint Contractor needs website

We need a website for our residential painting, multi-family painting and commercial painting company. We paint interior and exterior of houses, apartments and commercial buildings. I would like an about us page, residential page, multi family page, commercial page and contact us. Need keywords added to website for seo opitimazation. I like this website https://www.velmorandhalestudio.com/

Target Market(s)

General Contractors and commercial property managers

Coding

Coded - Design and coding required

Number of Pages Required

5+ page

Font styles to use
Sans Serif

Requirements
Must have
• I need SEO keywords on pages

```html
<!DOCTYPE html>
<html lang="en">
<head>
<meta charset="utf-8">
<title>Velmora Painting – Residential, Multi-Family &amp; Commercial Painting</title>
<link href="https://fonts.googleapis.com/css2?family=Poppins:wght@400;500;700&family=Lato:wght@400;700&display=swap" rel="stylesheet">
<style>
:root{
  --yellow:#f3dd63;
  --dark:#3b3b3b;
  --darker:#2f2f2f;
  --band:#5a5555;
  --ink:#1c1c1c;
  --muted:#9a9a9a;
  --pale:#eef0f5;
  --white:#ffffff;
}
*{margin:0;padding:0;box-sizing:border-box}
html,body{width:1200px;height:4237px;overflow:hidden;background:var(--white)}
body{position:relative;font-family:"Lato",sans-serif;color:var(--ink)}
.abs{position:absolute}
.head{font-family:"Poppins",sans-serif}

/* hero */
.hero{left:0;top:0;width:1200px;height:641px;background:linear-gradient(100deg,#f1f1f1 0%,#e2e2e4 45%,#c9ccd3 70%,#9aa6bb 100%)}
.topbar{left:0;top:0;width:1200px;height:71px;background:rgba(120,120,120,.75)}
.brand{left:46px;top:16px;color:var(--white);font-family:"Poppins",sans-serif;font-weight:700;font-size:26px;letter-spacing:1px;line-height:40px}
.burger{right:28px;top:26px;width:32px}
.hero-title{left:46px;top:205px;font-family:"Poppins",sans-serif;font-weight:700;font-size:46px;letter-spacing:1px}
.hero-sub{left:46px;top:268px;font-family:"Poppins",sans-serif;font-size:21px;letter-spacing:1px}
.hero-text{left:46px;top:322px;border-left:4px solid var(--ink);padding-left:20px;font-size:12px;line-height:22px;width:360px}
.btn{background:var(--yellow);font-family:"Poppins",sans-serif;font-size:13px;letter-spacing:1px;text-align:center;color:var(--ink)}
.hero-btn{left:46px;top:386px;width:182px;height:43px;line-height:43px}

/* features */
.feature{top:641px;width:300px;height:304px;background:var(--dark);color:var(--white);text-align:center}
.feature.alt{background:var(--darker)}
.feature svg{margin-top:68px;height:52px}
.feature h3{font-family:"Poppins",sans-serif;font-weight:400;font-size:23px;margin-top:12px}
.feature p{font-size:12px;line-height:22px;color:#a8a8a8;width:250px;margin:14px auto 0}
.feature .more{position:absolute;left:0;bottom:0;width:100%;height:47px;line-height:47px;background:var(--yellow);color:var(--ink);font-family:"Poppins",sans-serif;font-weight:500;font-size:15px}

/* section titles */
.sec-title{left:0;width:1200px;text-align:center;font-family:"Poppins",sans-serif;font-weight:700;font-size:44px;letter-spacing:2px}
.sec-text{left:350px;width:500px;text-align:center;font-size:11px;line-height:22px;color:var(--muted)}

.video{left:46px;top:1221px;width:539px;height:463px;background:linear-gradient(135deg,#8e8e90,#606064 60%,#4a4a4c)}
.play{left:271px;top:1411px}
.point{left:684px;width:472px;height:122px;background:var(--yellow);padding:22px 0 0 44px}
.point h4{font-family:"Poppins",sans-serif;font-weight:400;font-size:23px}
.point p{font-size:11.5px;line-height:22px;width:240px;margin-top:8px}

/* projects */
.projects{left:0;top:1831px;width:1177px;height:528px;background:var(--pale)}
.filter{top:1999px;font-size:13px;color:#8a8a8a}
.filter.on{color:#e0b93a}
.card{top:2047px;width:253px;height:215px;background:linear-gradient(135deg,#b7b5b0,#6b6b6f);}
.card .frame{position:absolute;left:15px;top:15px;right:15px;bottom:15px;border:2px solid rgba(255,255,255,.85);color:var(--white);text-align:center;padding-top:30px}
.card h5{font-family:"Poppins",sans-serif;font-weight:400;font-size:16px;line-height:22px}
.card p{font-size:12px;line-height:22px;margin:14px 10px 0}
.arrow{top:2132px;width:43px;height:43px;background:#e4e6ea}

/* partners */
.partners{left:0;top:2372px;width:1200px;height:258px;background:linear-gradient(90deg,#5c5858,#565151 50%,#5d5858)}
.partner{top:2460px;width:240px;text-align:center;color:var(--white);font-family:"Poppins",sans-serif;font-weight:500;font-size:30px}

/* brochure */
.broch-img{left:100px;top:2701px;width:337px;height:498px;background:linear-gradient(180deg,#f4f4f4,#e6e6e6 60%,#7fa58e 85%,#b7b7b7)}
.broch{left:547px;top:2708px;width:579px;height:503px;border:10px solid #eceef2;background:var(--white);text-align:center}
.broch h2{font-family:"Poppins",sans-serif;font-weight:700;font-size:45px;letter-spacing:1px;margin-top:90px}
.broch p{font-size:12px;line-height:22px;color:var(--muted);width:380px;margin:60px auto 0}
.broch .btn{display:inline-block;width:184px;height:42px;line-height:42px;margin-top:40px}

/* news */
.news{left:0;top:3321px;width:1200px;height:592px;background:var(--pale)}
.post{top:3507px;width:350px;height:310px;background:var(--white)}
.post .pic{position:absolute;left:0;top:0;width:181px;height:310px;background:linear-gradient(135deg,#e6e2dc,#b7a99a 60%,#8c7e72)}
.post .body{position:absolute;left:190px;top:28px;width:150px}
.post h5{font-family:"Poppins",sans-serif;font-weight:400;font-size:19px;line-height:24px}
.post .date{font-size:12px;margin:12px 0 20px}
.post p{font-size:12px;line-height:23px;color:var(--muted)}

/* footer */
.f-head{top:3980px;font-family:"Poppins",sans-serif;font-size:20px;letter-spacing:1px}
.f-line{font-size:12px}
.field{left:424px;top:4061px;width:268px;height:44px;border:1px solid #e3e3e3;font-size:11px;color:#aaa;padding:14px 0 0 18px}
.go{left:692px;top:4061px;width:64px;height:44px;background:var(--yellow)}
.social{top:4061px;width:44px;height:44px;border:1px solid #e4b9ab}
.social span{position:absolute;left:13px;top:13px;width:16px;height:16px;border-radius:50%;background:#e35b35}
.bottom{left:0;top:4176px;width:1200px;height:61px;background:var(--darker);color:#b5b5b5;font-size:12px}
.bottom a{position:absolute;top:26px;color:#b5b5b5;text-decoration:none;letter-spacing:1px}
</style>
</head>
<body>

<!-- Hero -->
<div class="abs hero" role="img" aria-label="Painter in white overalls rolling paint onto a bright interior wall"></div>
<div class="abs topbar"></div>
<div class="abs brand">VELMORA</div>
<svg class="abs burger" viewBox="0 0 32 26" aria-hidden="true"><rect y="0" width="32" height="3" fill="#fff"/><rect y="11" width="32" height="3" fill="#fff"/><rect y="22" width="32" height="3" fill="#fff"/></svg>
<h1 class="abs hero-title">LOREM IPSUM</h1>
<div class="abs hero-sub">NEMO ENIM IPSAM VOLUPTATEM</div>
<p class="abs hero-text">otam rem aperiam, eaque ipsa quae ab illo inventore veritatis et quasi architecto beatae vitae dicta sunt .</p>
<div class="abs btn hero-btn">READ MORE</div>

<!-- Features -->
<div class="abs feature" style="left:0">
  <svg viewBox="0 0 52 52" aria-hidden="true"><rect x="6" y="4" width="34" height="13" rx="2" fill="#fff"/><path d="M40 10h6v14H24v8" stroke="#fff" stroke-width="3" fill="none"/><rect x="20" y="32" width="8" height="18" rx="2" fill="#fff"/></svg>
  <h3>Recent Projects</h3>
  <p>At vero eos et accusamus et iusto odio dignissimos ducimus qui blanditiis praesentium voluptatum deleniti</p>
</div>
<div class="abs feature alt" style="left:300px">
  <svg viewBox="0 0 52 52" aria-hidden="true"><rect x="4" y="4" width="16" height="42" rx="2" fill="#fff"/><path d="M22 14l12 -6 12 26-24 12z" fill="#fff"/><circle cx="12" cy="38" r="3" fill="#2f2f2f"/></svg>
  <h3>Perfect Color</h3>
  <p>Nam libero tempore, cum soluta nobis est eligendi optio cumque nihil impedit quo minus id quod maxime placeat facere</p>
</div>
<div class="abs feature" style="left:600px">
  <svg viewBox="0 0 52 52" aria-hidden="true"><path d="M30 22l14-14 4 4-14 14z" fill="#fff"/><path d="M10 28l10-8 12 12-8 10z" fill="#fff"/><path d="M10 30l-6 16 16-6z" fill="#fff"/></svg>
  <h3>Our Process</h3>
  <p>At vero eos et accusamus et iusto odio dignissimos ducimus qui blanditiis praesentium voluptatum deleniti</p>
</div>
<div class="abs feature alt" style="left:900px">
  <svg viewBox="0 0 52 52" aria-hidden="true"><g fill="#fff"><rect x="4" y="6" width="20" height="10"/><rect x="28" y="6" width="20" height="10"/><rect x="4" y="20" width="12" height="10"/><rect x="20" y="20" width="12" height="10"/><rect x="36" y="20" width="12" height="10"/><rect x="4" y="34" width="20" height="10"/><rect x="28" y="34" width="20" height="10"/></g></svg>
  <h3>Other Services</h3>
  <p>Nam libero tempore, cum soluta nobis est eligendi optio cumque nihil impedit quo minus id quod maxime</p>
  <div class="more">READ MORE</div>
</div>

<!-- About -->
<h2 class="abs sec-title" style="top:1060px">ABOUT US</h2>
<p class="abs sec-text" style="top:1131px">Ante Morbi eget arcurmentum vel congue id euismod in elit Fusce ultricies orci ac feugiat suscipit leo. Ante Morbi eget arcurmentum vel congue id euismod in elit Fusce ultricies orci ac feugiat suscipit leo</p>
<div class="abs video" role="img" aria-label="Video still of a painter in a cap rolling paint onto a ceiling"></div>
<svg class="abs play" width="86" height="86" viewBox="0 0 86 86" aria-hidden="true"><circle cx="43" cy="43" r="42" fill="rgba(255,255,255,.45)"/><circle cx="43" cy="43" r="32" fill="#fff"/><path d="M36 30l18 13-18 13z" fill="#555"/></svg>
<div class="abs point" style="top:1221px"><h4>Years of Experience</h4><p>With 17+ years of experience, we provide the best services</p></div>
<div class="abs point" style="top:1368px"><h4>Qualified Team</h4><p>Augiat in pede Fusce tellus Sed metus augue convallis et vehicula</p></div>
<div class="abs point" style="top:1514px"><h4>Quality Materials</h4><p>Augiat in pede Fusce tellus Sed metus augue convallis et vehicula</p></div>

<!-- Projects -->
<div class="abs projects"></div>
<h2 class="abs sec-title" style="top:1915px;width:1177px">OUR PROJECTS</h2>
<span class="abs filter on" style="left:350px">ALL</span>
<span class="abs filter" style="left:442px">RESIDENTIAL</span>
<span class="abs filter" style="left:583px">COMMERCIAL</span>
<span class="abs filter" style="left:756px">PROJECT</span>
<div class="abs arrow" style="left:13px"><svg width="43" height="43" aria-hidden="true"><path d="M25 14l-8 8 8 8" stroke="#bbb" stroke-width="2" fill="none"/></svg></div>
<div class="abs arrow" style="left:1143px"><svg width="43" height="43" aria-hidden="true"><path d="M18 14l8 8-8 8" stroke="#bbb" stroke-width="2" fill="none"/></svg></div>
<div class="abs card" style="left:66px" role="img" aria-label="Bright painted living room interior"><div class="frame"><h5>INTERIOR HOUSE<br>PAINTING</h5><p>Ut enim ad minima veniam, quis nostrum exercitationem ullam corporis suscipit laboriosam</p></div></div>
<div class="abs card" style="left:339px;background:linear-gradient(135deg,#5d6460,#3d4440)" role="img" aria-label="Modern building exterior with glass walls"><div class="frame"><h5>EXTERIOR BUILDING<br>PAINTING</h5><p>Quis autem vel eum iure reprehenderit qui in ea voluptate</p></div></div>
<div class="abs card" style="left:612px;background:linear-gradient(135deg,#c9c9c9,#9a9a9c)" role="img" aria-label="Freshly painted white building interior"><div class="frame"><h5>INTERIOR BUILDING<br>PAINTING</h5><p>Vel illum qui dolorem eum fugiat quo voluptas nulla pariatur</p></div></div>
<div class="abs card" style="left:883px;background:linear-gradient(135deg,#6e655c,#3f4246)" role="img" aria-label="Recently painted modern house"><div class="frame"><h5>RECENT PROJECT<br>PAINTING</h5><p>Nemo enim ipsam voluptatem quia voluptas sit aspernatur aut odit aut fugit</p></div></div>

<!-- Partners -->
<div class="abs partners" role="img" aria-label="Dimmed photo of a painter at work behind partner names"></div>
<div class="abs partner" style="left:53px">LINEMARK</div>
<div class="abs partner" style="left:339px;font-size:22px;top:2468px">CRESTLINE</div>
<div class="abs partner" style="left:620px">Openfield</div>
<div class="abs partner" style="left:907px;font-size:24px;top:2466px">Northgate</div>

<!-- Brochure -->
<div class="abs broch-img" role="img" aria-label="Painter in white holding an open colour brochure"></div>
<div class="abs broch">
  <h2>GET OUR BROCHURE</h2>
  <p>If you are looking for a high-quality construction services provider, we'd be glad to help you. Download our Brochure to learn more about our prices and range of services.</p>
  <div class="btn">DOWNLOAD</div>
</div>

<!-- News -->
<div class="abs news"></div>
<h2 class="abs sec-title" style="top:3406px">COMPANY NEWS</h2>
<div class="abs post" style="left:46px"><div class="pic" role="img" aria-label="Couple painting a room wall together"></div><div class="body"><h5>Sed quia numquam, cum soluta</h5><div class="date">May 16, 2020</div><p>Nam libero tempore, cum soluta nobis est eligendi optio cumque nihil impedit quo minus id quod maxime .</p></div></div>
<div class="abs post" style="left:424px"><div class="pic" role="img" aria-label="Couple with a ladder and paint roller in a new home"></div><div class="body" style="top:16px"><h5>Nam libero tempore. Soluta nobis</h5><div class="date">May 22, 2020</div><p>Temporibus autem quibusdam et aut officiis debitis aut rerum necessitatibus saepe eveniet</p></div></div>
<div class="abs post" style="left:804px"><div class="pic" style="background:linear-gradient(135deg,#f0eee8,#d8cfa8 55%,#8a8f84)" role="img" aria-label="Paint cans, rollers and brushes on the floor"></div><div class="body"><h5>Et harum quidem rerum facilis</h5><div class="date">July 01, 2020</div><p>Temporibus autem quibusdam et aut officiis debitis aut rerum necessitatibus saepe eveniet</p></div></div>

<!-- Footer -->
<div class="abs f-head" style="left:46px">CONTACT US</div>
<div class="abs f-line" style="left:46px;top:4034px">+1 (555) 014-2290</div>
<div class="abs f-line" style="left:46px;top:4062px;font-size:11px">info@velmorapainting.com</div>
<div class="abs f-line" style="left:46px;top:4090px;font-size:11px">4120 Alder Rd., Fairview, VA, 22300</div>

<div class="abs f-head" style="left:424px">SUBSCRIBE</div>
<div class="abs f-line" style="left:424px;top:4031px;font-size:11px">Enter your e-mail to receive the latest news from us.</div>
<div class="abs field">Your E-mail</div>
<div class="abs go"></div>

<div class="abs f-head" style="left:898px">SOCIAL LINKS</div>
<div class="abs f-line" style="left:898px;top:4031px;font-size:11px">Follow us on these social networks.</div>
<div class="abs social" style="left:901px"><span></span></div>
<div class="abs social" style="left:960px"><span></span></div>
<div class="abs social" style="left:1019px"><span></span></div>
<div class="abs social" style="left:1078px"><span></span></div>

<nav class="abs bottom">
  <a style="left:46px">HOME</a>
  <a style="left:146px">SERVICES</a>
  <a style="left:268px">ABOUT US</a>
  <a style="left:396px">PROJECTS</a>
  <a style="left:521px">CONTACT US</a>
  <span class="abs" style="right:64px;top:27px;font-size:11px">© 2020 &nbsp;Velmora Painting</span>
</nav>

</body>
</html>
```